QuadLantern--Help Us look fresh and new to companies, college students and college career centers!

We just designed a new logo and would like to freshen-up and make our business cards a bit more modern. Not crazy-modern like Picasso, but modern like metro-style and fresh like fruit. We use three logos with a combination of two colors each, and three colors total. We are looking for a single format to apply to three different cards/color schemes (green/blue to give out to companies, orange/green for students, and orange/blue for university career centers). Thanks everyone--looking forward to seeing your designs!!

Target Market(s)

Three styles: companies, college students/grads, college career centers

Industry/Entity Type

College

Contact Information for Business Card

Address: 1187 9th Avenue, Suite 614, Seattle, WA 98104. Need a spot for email address, web address (www.quadlantern-example.com), and phone numbers (main, direct, mobile). Don't open that website unless you want to lose your lunch--it is waaaay old and outdated. See this link instead, http://staging.brixelworks-example.com/QuadLantern/EmployerSolutions, for our new website design in progress.

Font styles to use
Sans Serif

Requirements
Must have
• Please use the logos supplied. Would like text to be grey but printable, like a "light" type style that is metro-type with sans-serif. NOT black text. Modern. For inspiration, here's a link to our work-in-progress website we are planning to launch soon: http://staging.brixelworks-example.com/QuadLantern/EmployerSolutions
Nice to have
• Would like to see something unique and different in a "metro" style. Clean and not cluttered.
Should not have
• No odd-sized cards

```html
<!DOCTYPE html>
<html lang="en">
<head>
<meta charset="utf-8">
<title>QuadLantern Business Card</title>
<link rel="stylesheet" href="https://fonts.googleapis.com/css2?family=Lato:wght@300;400;700&display=swap">
<style>
  :root {
    --page: #ecebe7;
    --card: #ffffff;
    --green: #7cc242;
    --green-light: #b9e07f;
    --orange: #f5a623;
    --ink: #5f6770;
    --shadow: rgba(0, 0, 0, 0.14);
  }
  html, body {
    margin: 0;
    width: 1200px;
    height: 1023px;
    overflow: hidden;
    background: var(--page);
    font-family: "Lato", sans-serif;
  }
  .sheet {
    position: relative;
    width: 1200px;
    height: 1023px;
  }
  .card {
    position: absolute;
    left: 240px;
    width: 720px;
    height: 411px;
    border-radius: 22px;
    overflow: hidden;
    background: var(--card);
    box-shadow: 0 10px 28px var(--shadow);
  }
  .card--front { top: 62px; }
  .card--back { top: 550px; }
  .card svg { display: block; width: 720px; height: 411px; }
  .brand-name { font-family: "Lato", sans-serif; font-weight: 700; fill: var(--orange); }
  .brand-name--back { fill: var(--green); }
  .contact-label, .contact-value, .contact-address {
    font-family: "Lato", sans-serif;
    font-weight: 300;
    fill: var(--ink);
    font-size: 18px;
  }
  .contact-address { font-weight: 400; }
</style>
</head>
<body>
<main class="sheet">

  <section class="card card--front" aria-label="Business card front">
    <svg viewBox="0 0 720 411" xmlns="http://www.w3.org/2000/svg">
      <defs>
        <linearGradient id="bandGreen" x1="0" y1="0" x2="1" y2="1">
          <stop offset="0" stop-color="var(--green-light)"/>
          <stop offset="0.55" stop-color="var(--green)"/>
          <stop offset="1" stop-color="var(--green)"/>
        </linearGradient>
      </defs>
      <path class="accent-line" d="M60,411 Q340,170 720,6" fill="none" stroke="var(--orange)" stroke-width="5"/>
      <path class="info-band" d="M80,411 Q360,180 720,20 L720,411 Z" fill="url(#bandGreen)"/>

      <g class="brand">
        <circle cx="62" cy="112" r="20" fill="var(--green)"/>
        <text class="brand-name" x="94" y="132" font-size="58">QuadLantern</text>
      </g>

      <g class="contact">
        <text class="contact-label" x="380" y="222">Main:</text>
        <text class="contact-value" x="450" y="222">333-222-1111</text>
        <text class="contact-label" x="380" y="247">Direct:</text>
        <text class="contact-value" x="450" y="247">333-222-1111</text>
        <text class="contact-label" x="380" y="272">Mobile:</text>
        <text class="contact-value" x="450" y="272">333-222-1111</text>
        <text class="contact-label" x="380" y="297">Email:</text>
        <text class="contact-value" x="450" y="297">info@quadlantern.com</text>
        <text class="contact-label" x="380" y="322">Web:</text>
        <text class="contact-value" x="450" y="322">www.quadlantern-example.com</text>
        <text class="contact-address" x="690" y="376" text-anchor="end">1187 9th Avenue, Suite 614, Seattle, WA 98104.</text>
      </g>
    </svg>
  </section>

  <section class="card card--back" aria-label="Business card back">
    <svg viewBox="0 0 720 411" xmlns="http://www.w3.org/2000/svg">
      <path class="accent-line" d="M222,0 Q318,200 262,411" fill="none" stroke="var(--orange)" stroke-width="5"/>
      <path class="side-band" d="M0,0 L200,0 Q296,200 240,411 L0,411 Z" fill="var(--green)"/>
      <text class="brand-name brand-name--back" x="680" y="228" font-size="60" text-anchor="end">QuadLantern</text>
    </svg>
  </section>

</main>
</body>
</html>
```